brake hoses

revamp current brake hose flyer - modernize make it look better

please use website
Kestrelmotorworks.co.nz for as much as possible

i want you all to come with own wording description etc

```html
<!DOCTYPE html>
<html lang="en">
<head>
<meta charset="utf-8">
<title>Kestrel Motorworks – Hose Range Flyer</title>
<link rel="stylesheet" href="https://fonts.googleapis.com/css2?family=Bebas+Neue&family=Montserrat:wght@300;600;700;800&display=swap">
<style>
  :root{
    --backdrop:#8d8d8d;
    --yellow:#ffd800;
    --yellow-photo:#d9c21a;
    --ink:#111111;
    --white:#ffffff;
    --grey-band:#dedede;
    --grey-soft:#ececec;
  }
  *{box-sizing:border-box;margin:0;padding:0}
  html,body{width:1200px;height:1200px;overflow:hidden;background:var(--backdrop)}
  .flyer{position:absolute;left:243px;top:98px;width:713px;height:1008px;background:var(--white);overflow:hidden;font-family:"Montserrat",sans-serif;color:var(--ink)}
  .warehouse-photo{position:absolute;left:0;top:0;width:713px;height:354px;
    background:radial-gradient(ellipse at 55% 35%,#f3e46a 0%,#d8c11e 45%,#a8920c 100%)}
  .workshop-photo{position:absolute;left:0;top:354px;width:713px;height:247px;
    background:linear-gradient(90deg,#ffffff 0%,#ffffff 45%,#e6e6e6 80%,#d2d2d2 100%)}
  .product{position:absolute;border-radius:50%}
  .product .shadow{position:absolute;inset:0;border-radius:50%;background:var(--ink);transform:translate(-7px,6px)}
  .product .shot{position:absolute;inset:0;border-radius:50%;background:radial-gradient(circle at 50% 50%,#ffffff 0%,#f4f4f4 60%,#e2e2e2 100%)}
  .product-brackets{left:81px;top:26px;width:136px;height:136px}
  .product-rubber{left:231px;top:64px;width:156px;height:156px}
  .product-braided{left:37px;top:174px;width:224px;height:224px}
  .brand-frame{position:absolute;left:433px;top:260px;width:246px;height:178px;background:var(--white)}
  .brand-tile{position:absolute;left:12px;top:9px;width:222px;height:161px;background:var(--yellow);
    display:flex;flex-direction:column;align-items:center;justify-content:center;gap:12px}
  .brand-mark{width:34px;height:34px;background:var(--ink)}
  .brand-name{font-weight:800;font-size:17px;letter-spacing:.5px;color:var(--ink)}
  .specialty{position:absolute;left:463px;top:452px;width:200px;text-align:center;font-weight:800;font-size:20px;line-height:26px}
  .headline-band{position:absolute;left:43px;top:494px;width:392px;height:74px;background:var(--yellow)}
  .headline-large{position:absolute;left:54px;top:418px;font-family:"Bebas Neue",sans-serif;font-size:116px;line-height:1;color:var(--ink);letter-spacing:-1px}
  .headline-sub{position:absolute;left:93px;top:513px;font-weight:700;font-size:38px;line-height:1}
  .headline-rule{position:absolute;left:158px;top:574px;width:275px;height:3px;background:var(--ink)}
  .hose-types{position:absolute;left:0;top:601px;width:713px;height:215px;background:var(--grey-band)}
  .hose-type{position:absolute;display:flex;align-items:center;gap:20px;font-family:"Bebas Neue",sans-serif;font-size:29px;line-height:1}
  .hose-type svg{width:44px;height:44px;flex:none}
  .aim{position:absolute;left:0;top:833px;width:713px;height:94px;background:var(--ink);color:var(--white);
    text-align:center;padding-top:14px;font-weight:700;font-size:20px;line-height:27px}
  .aim .lead{color:var(--yellow);font-weight:300;font-size:27px}
  .contact{position:absolute;left:36px;top:954px;width:650px;display:flex;justify-content:space-between;font-size:12px;font-weight:600;line-height:16px}
  .contact b{font-weight:800}
  .contact .sep{width:3px;height:12px;background:var(--yellow);margin-top:2px}
  .contact .address{text-align:right}
  .footer-bar{position:absolute;left:0;top:993px;width:713px;height:15px;background:var(--yellow)}
</style>
</head>
<body>
<main class="flyer">
  <div class="warehouse-photo" role="img" aria-label="Parts warehouse aisle with stocked shelving, tinted yellow"></div>
  <div class="workshop-photo" role="img" aria-label="Faded photo of a technician crimping a hose"></div>

  <div class="product product-brackets"><span class="shadow"></span><span class="shot" role="img" aria-label="Metal hose brackets and clips"></span></div>
  <div class="product product-rubber"><span class="shadow"></span><span class="shot" role="img" aria-label="Set of rubber brake hoses"></span></div>
  <div class="product product-braided"><span class="shadow"></span><span class="shot" role="img" aria-label="Braided stainless hose with banjo fittings"></span></div>

  <div class="brand-frame">
    <div class="brand-tile">
      <span class="brand-mark"></span>
      <span class="brand-name">KESTREL MOTORWORKS</span>
    </div>
  </div>

  <p class="specialty">Specialise in the Manufacture of Rubber &amp; Braided Hoses</p>

  <div class="headline-band"></div>
  <h1 class="headline-large">LARGE</h1>
  <p class="headline-sub">range of Hoses</p>
  <div class="headline-rule"></div>

  <section class="hose-types">
    <div class="hose-type" style="left:43px;top:14px">
      <svg viewBox="0 0 44 44"><circle cx="22" cy="22" r="21" fill="#111"/><circle cx="22" cy="22" r="16" fill="none" stroke="#ffd800" stroke-width="1.5"/><path d="M22 12 C18 19 16 22 16 25 a6 6 0 0 0 12 0 c0-3-2-6-6-13z" fill="#ffd800"/></svg>OIL</div>
    <div class="hose-type" style="left:253px;top:14px">
      <svg viewBox="0 0 44 44"><circle cx="22" cy="22" r="21" fill="#111"/><circle cx="22" cy="22" r="16" fill="none" stroke="#ffd800" stroke-width="1.5"/><rect x="15" y="13" width="10" height="18" rx="1" fill="#ffd800"/><rect x="17" y="15" width="6" height="5" fill="#111"/><path d="M25 18 h3 v9 a1.5 1.5 0 0 0 3 0 v-10 l-2-2" fill="none" stroke="#ffd800" stroke-width="1.6"/></svg>FUEL</div>
    <div class="hose-type" style="left:483px;top:14px">
      <svg viewBox="0 0 44 44"><circle cx="22" cy="22" r="21" fill="#111"/><circle cx="22" cy="22" r="16" fill="none" stroke="#ffd800" stroke-width="1.5"/><circle cx="22" cy="23" r="9" fill="#ffd800"/><circle cx="22" cy="23" r="2.5" fill="#111"/><path d="M13 17 a11 11 0 0 1 10-6" fill="none" stroke="#ffd800" stroke-width="3"/></svg>BRAKE</div>
    <div class="hose-type" style="left:43px;top:82px">
      <svg viewBox="0 0 44 44"><circle cx="22" cy="22" r="21" fill="#111"/><circle cx="22" cy="22" r="16" fill="none" stroke="#ffd800" stroke-width="1.5"/><path d="M14 30 L27 17 M24 13 l7 7 M17 27 l-3 -6" stroke="#ffd800" stroke-width="3" stroke-linecap="round" fill="none"/></svg>BRAIDED</div>
    <div class="hose-type" style="left:253px;top:82px">
      <svg viewBox="0 0 44 44"><circle cx="22" cy="22" r="21" fill="#111"/><circle cx="22" cy="22" r="16" fill="none" stroke="#ffd800" stroke-width="1.5"/><circle cx="22" cy="22" r="10" fill="none" stroke="#ffd800" stroke-width="2.5"/><circle cx="22" cy="22" r="2.5" fill="#ffd800"/><path d="M12 21 h20 M22 22 v10" stroke="#ffd800" stroke-width="2.5"/></svg>POWERSTEERING</div>
    <div class="hose-type" style="left:483px;top:82px">
      <svg viewBox="0 0 44 44"><circle cx="22" cy="22" r="21" fill="#111"/><circle cx="22" cy="22" r="16" fill="none" stroke="#ffd800" stroke-width="1.5"/><rect x="12" y="15" width="20" height="8" rx="1.5" fill="#ffd800"/><path d="M14 27 l-1 3 M18 27 l-1 3 M22 27 l-1 3 M26 27 l-1 3 M30 27 l-1 3" stroke="#ffd800" stroke-width="1.4"/></svg>AIR CONDITIONING</div>
    <div class="hose-type" style="left:43px;top:151px">
      <svg viewBox="0 0 44 44"><circle cx="22" cy="22" r="21" fill="#111"/><circle cx="22" cy="22" r="16" fill="none" stroke="#ffd800" stroke-width="1.5"/><path d="M13 18 h7 v10 h6 v-6 h5 M29 22 v8" fill="none" stroke="#ffd800" stroke-width="2.5" stroke-linejoin="round"/></svg>BRAKE AND FUEL PIPES AND FITTINGS</div>
  </section>

  <section class="aim">
    <p><span class="lead">OUR AIM</span> is to have your parts repaired with the quickest<br>turn-around times possible</p>
  </section>

  <footer class="contact">
    <span><b>Phone:</b> 0800 55 41 82</span>
    <span class="sep"></span>
    <span><b>Email:</b> parts@kestrelmotorworks.co.nz</span>
    <span class="sep"></span>
    <span class="address"><b>Address:</b> 27 Harwood Lane,<br>Millbrook, Hamilton</span>
  </footer>
  <div class="footer-bar"></div>
</main>
</body>
</html>
```